Business Card for Coach - ready to print

Design Business Card ready to order prints www.larsholm.coach

* An Overview / Background of the Business & Services
· Coaching
· Personal growth
* The Target Market / Audience you are trying to reach
· private person in different roles (self, familiy, business role)s
* Design Specifics; any preferences or ideas for Style, Colour, Imagery, etc
· See www.larsholm.coach
· "simple" design
· (small) element of surprise / unusual element

* Information that will be placed in the Business Card
· Beratung und Coaching
· Address: Lars Holm, Kesselgasse 7, CH-8517 Winterthur, Mobile +41 76 254 60 31
* Do you have an existing website or Facebook page where designers can learn more about your company?
· larsholm.coach

Target Market(s)

private person in different roles (self, familiy, business role)

Industry/Entity Type

Life Coaching

Contact Information for Business Card

Lars Holm
Kesselgasse 7
CH-8517 Winterthur

Mobile: +41 76 254 60 31
Email: laho@mailvale.ch
www.larsholm.coach

Font styles to use
Sans Serif

Colors

Designer to choose colors to be used in the design.

Requirements
Must have
• "simple" design
• element of surprise / unusual element
• Weg & Wandel
• see www.larsholm.coach for colors and so...
Nice to have
• TA Symbol (three rings on top of each other) - unsual presentation
• QR Code of Website (see if it fits in and still looks good).

```html
<!DOCTYPE html>
<html lang="de">
<head>
<meta charset="utf-8">
<title>Weg &amp; Wandel – Visitenkarte</title>
<link rel="stylesheet" href="https://fonts.googleapis.com/css2?family=Montserrat:wght@300;400;500&display=swap">
<style>
  :root {
    --page-bg: #1c1f24;
    --card-bg: #3a3a3b;
    --brand-orange: #f39a1e;
    --pale-blue: #a9d4ef;
    --text-light: #e4e6e8;
    --divider: #8a8d90;
    --stripe-white: #f4f4f4;
  }
  * { margin: 0; padding: 0; box-sizing: border-box; }
  html, body { width: 1200px; height: 900px; overflow: hidden; }
  body {
    background: var(--page-bg);
    font-family: "Montserrat", sans-serif;
    display: flex;
    align-items: center;
    justify-content: center;
    gap: 48px;
  }
  .card {
    position: relative;
    width: 530px;
    height: 330px;
    background: var(--card-bg);
    border-radius: 3px;
    overflow: hidden;
    box-shadow: 0 18px 40px rgba(0,0,0,.45);
  }

  /* Front */
  .card--front {
    display: flex;
    align-items: center;
    justify-content: center;
  }
  .brand-name {
    font-weight: 400;
    text-transform: uppercase;
    white-space: nowrap;
  }
  .card--front .brand-name {
    font-size: 26px;
    letter-spacing: .1em;
    color: var(--brand-orange);
  }

  /* Back */
  .back__brand {
    position: absolute;
    left: 34px; top: 118px;
    width: 150px;
    text-align: center;
  }
  .back__brand .brand-name {
    font-size: 14px;
    letter-spacing: .1em;
    color: var(--pale-blue);
  }
  .back__divider {
    position: absolute;
    left: 205px; top: 70px;
    width: 1px; height: 140px;
    background: var(--divider);
  }
  .contact {
    position: absolute;
    left: 228px; top: 66px;
  }
  .contact__name {
    font-weight: 400;
    font-size: 27px;
    letter-spacing: .08em;
    text-transform: uppercase;
    color: var(--pale-blue);
    line-height: 1;
  }
  .contact__role {
    font-weight: 400;
    font-size: 14px;
    color: var(--pale-blue);
    margin: 4px 0 12px;
  }
  .contact__list { list-style: none; }
  .contact__item {
    display: flex;
    align-items: center;
    gap: 10px;
    font-size: 14.5px;
    color: var(--text-light);
    line-height: 24px;
  }
  .contact__icon { width: 14px; height: 14px; flex: none; }
  .address {
    position: absolute;
    left: 34px; bottom: 36px;
    font-size: 15px;
    color: var(--text-light);
  }
  .edge-stripe {
    position: absolute;
    left: 0; right: 0; bottom: 0;
    height: 6px;
    display: flex;
  }
  .edge-stripe__white { width: 38%; background: var(--stripe-white); }
  .edge-stripe__blue { flex: 1; background: var(--pale-blue); }
</style>
</head>
<body>

  <section class="card card--back" aria-label="Visitenkarte Rückseite">
    <div class="back__brand">
      <span class="brand-name">Weg &amp; Wandel</span>
    </div>
    <div class="back__divider"></div>

    <div class="contact">
      <h1 class="contact__name">Lars Holm</h1>
      <p class="contact__role">President</p>
      <ul class="contact__list">
        <li class="contact__item">
          <svg class="contact__icon" viewBox="0 0 16 16" fill="none" stroke="#e4e6e8" stroke-width="1.3">
            <circle cx="8" cy="8" r="7"/>
            <path d="M5.5 4.5l1.5 1.8-.8 1c.6 1.1 1.3 1.8 2.4 2.4l1-.8 1.8 1.5-.9 1.2c-2.6-.4-5.2-3-5.6-5.6z"/>
          </svg>
          +41 76 254 60 31
        </li>
        <li class="contact__item">
          <svg class="contact__icon" viewBox="0 0 16 16" fill="none" stroke="#e4e6e8" stroke-width="1.3">
            <rect x="1.5" y="3.5" width="13" height="9"/>
            <path d="M1.5 3.5L8 9l6.5-5.5M1.5 12.5l5-4.5M14.5 12.5l-5-4.5"/>
          </svg>
          laho@mailvale.ch
        </li>
        <li class="contact__item">
          <svg class="contact__icon" viewBox="0 0 16 16" fill="none" stroke="#e4e6e8" stroke-width="1.3">
            <circle cx="8" cy="8" r="6.5"/>
            <ellipse cx="8" cy="8" rx="3" ry="6.5"/>
            <path d="M1.5 8h13M2.5 4.8h11M2.5 11.2h11"/>
          </svg>
          www.larsholm.coach
        </li>
      </ul>
    </div>

    <p class="address">Kesselgasse 7, CH-8517 Winterthur</p>

    <div class="edge-stripe">
      <span class="edge-stripe__white"></span>
      <span class="edge-stripe__blue"></span>
    </div>
  </section>

  <section class="card card--front" aria-label="Visitenkarte Vorderseite">
    <span class="brand-name">Weg &amp; Wandel</span>
  </section>

</body>
</html>
```